Design an engaging, visually attractive and well laid out Word Press website

I have a partially completed Word Press website that I need to have completed . The previous designer overestimated her ability to produce a quality product and underestimated my knowledge of how a good well designed website should look visually and be laid out.

A visitor to the site should have a clear understanding of the services offered by the business, be able to navigate the site with ease via effective logical pathways, have calls to action that are prominent and located in the correct locations that prompt the viewer to make contact when they are ready to act. The site needs to be visually impactful, have lots of white space, fast loading and mobile compatible and the visitor needs to have the impression that they need to look no further for the services offered.

I am particularly interested in how you think the Services and Projects pages should be best laid out so they present well on a mobile device without looking cluttered and can be navigated and viewed with ease.

I have the copy and images (these may need some changes) and I have put together a basic version of a layout on MS Word documents. These are all in a Dropbox folder (link below). I am open to a designer offering his/her own thoughts on how the site can be laid out better. Also I have a link below to the partially created website. I will need the website coded once I am happy with the design.

Links:

https://larkvale.com.au?bypass=moor

https://www.filecrate.net/sh/qwprtz8m3x204kd/BBXQwerTyuIopAsDfGhJkL-9z?dl=0

Target Market(s)

Primarily females aged 19 - 65 who work for a strata management and/or a property management company. These organisations oversee the maintenance aspects for apartments/condominiums and manage the properties on behalf of the owners.
The business that the website represents provides professional gardening services for commercial businesses and these apartment/condominium communities. So do not think home gardens and that type of gardening. Think on a larger scale like commercial businesses, hospitals, blocks of units/apartments/condominiums, shopping centres.

Industry/Entity Type

Commercial

Coding

Coded - Design and coding required

Number of Pages Required

5+ page

Requirements
Must have
• A great layout with lots of white space, intuitive navigation, prominent calls to action and professional looking.

The website needs to give the impression that the business is mid-size with a number of employees i.e. 6-10, yet still have the impression that it is a business where the owner is involved and there is a high level of personalised customer service.
Nice to have
• Maybe a looping video on the home page that is faded in the background that represents what the business does and who it services.
Should not have
• An attitude by the designer that anything will satisfy me. I want the designer to create a design that they would be proud to present to the market.

I have had too many bad experiences with website designers who do not have the appropriate attitude or skills to produce a quality site that appeals to me.

```html
<!DOCTYPE html>
<html lang="en">
<head>
<meta charset="utf-8">
<title>Larkvale – Garden Care mobile screens</title>
<link href="https://fonts.googleapis.com/css2?family=Oswald:wght@400;500&family=Lato:wght@400;700&display=swap" rel="stylesheet">
<style>
:root{
  --green:#7dbb3c;
  --green-dark:#5f9a2a;
  --ink:#222;
  --text:#555;
  --muted:#999;
  --panel:#f2f2f2;
  --tile:#efefef;
  --head:#1f1f1f;
  --footer:#111;
  --photo-green:#6f9a45;
  --photo-earth:#8a8670;
}
*{box-sizing:border-box;margin:0;padding:0}
html,body{width:1200px;height:579px;overflow:hidden;background:#fff}
body{position:relative;font-family:'Lato',sans-serif;color:var(--text)}
.screen{position:absolute;top:105px;width:171px;height:370px;overflow:hidden;background:#fff;border-radius:10px;box-shadow:0 0 0 1px #e4e4e4}
.abs{position:absolute}
.h-oswald{font-family:'Oswald',sans-serif;font-weight:500;color:var(--ink)}
.para{font-size:5.2px;line-height:11px;color:var(--text)}
.brand{font-family:'Oswald',sans-serif;font-weight:500;color:var(--green);letter-spacing:.5px;display:flex;align-items:center;gap:4px}
.brand i{display:block;background:var(--green)}
.prog{position:absolute;left:10px;width:150px;height:22px;background:var(--tile);font-family:'Oswald',sans-serif;font-size:6.3px;color:var(--ink);display:flex;align-items:center;justify-content:space-between;padding:0 8px 0 7px;text-transform:uppercase}
.prog::after{content:"";border-left:3px solid currentColor;border-top:2.2px solid transparent;border-bottom:2.2px solid transparent}
.prog.is-active{background:var(--green);color:#fff}
.photo{position:absolute}
.feat{position:absolute;display:flex;gap:7px;font-size:5px;line-height:8px;color:var(--ink);align-items:center}
.feat span{display:flex;align-items:center;gap:3px}
.feat svg{width:11px;height:11px;flex:none}
/* screen 1 */
.s1-head{left:0;top:0;width:171px;height:47px;background:var(--head)}
.menu-btn{right:15px;top:20px;width:15px;height:15px;background:var(--green);display:flex;flex-direction:column;justify-content:center;gap:1.6px;padding:0 4px}
.menu-btn b{display:block;height:1px;background:#fff}
.s1-hero{left:0;top:47px;width:171px;height:131px;background:var(--panel)}
.crumbs{font-size:5px;color:var(--muted);font-family:'Oswald',sans-serif;display:flex;gap:5px}
.crumbs em{font-style:normal;color:var(--green)}
/* screen 4 */
.cta-box{left:10px;top:233px;width:151px;height:94px;background:linear-gradient(#f5f5f5 70%,#eef3e6)}
.cta-title{font-family:'Oswald',sans-serif;color:var(--green);font-size:8.3px;text-align:center;width:100%;top:20px}
.btn{background:var(--green);color:#fff;font-family:'Oswald',sans-serif;font-size:5.4px;display:flex;align-items:center;justify-content:center}
.pager{font-family:'Oswald',sans-serif;font-size:5.6px}
/* screen 5 */
.s5{background:var(--footer);color:#fff}
.foot-h{font-family:'Oswald',sans-serif;font-weight:500;font-size:9.5px;color:#fff}
.rule{height:1px;width:15px;background:var(--green)}
.foot-link{font-size:5.6px;color:#fff}
.social{width:13px;height:13px;background:#555}
</style>
</head>
<body>

<!-- Screen 1: Garden care overview -->
<section class="screen" style="left:83px">
  <header class="abs s1-head">
    <div class="abs brand" style="left:11px;top:20px;font-size:7px"><i style="width:6px;height:6px"></i>LARKVALE</div>
    <div class="abs menu-btn"><b></b><b></b><b></b></div>
  </header>
  <div class="abs s1-hero"></div>
  <h1 class="abs h-oswald" style="left:10px;top:72px;font-size:11px;color:#5d6b6b;font-weight:400">GARDEN CARE</h1>
  <p class="abs para" style="left:10px;top:95px;width:152px">Our garden care service offers individually tailored programs so your garden looks great all the year round. Regular visits are scheduled depending upon the needs and the budgets of the individual clients.</p>
  <nav class="abs crumbs" style="left:10px;top:145px"><span>Home</span><span>»</span><span>Services</span><span>»</span><em>Garden Care</em></nav>
  <h2 class="abs h-oswald" style="left:10px;top:203px;font-size:11px;font-weight:400">Our Programs</h2>
  <p class="abs para" style="left:10px;top:225px;font-size:5.5px">View all we have to offer in our garden care programs</p>
  <div class="prog" style="top:245px">Lawn Care</div>
  <div class="prog" style="top:271px">Pruning &amp; Hedging</div>
  <div class="prog is-active" style="top:297px">Weed Control</div>
  <div class="prog" style="top:324px">Couch Grass Eradication</div>
  <div class="prog" style="top:350px">Soil Improvement</div>
</section>

<!-- Screen 2: Weed control detail -->
<section class="screen" style="left:300px">
  <div class="prog" style="top:6px">Fertilizing</div>
  <div class="prog" style="top:32px">Mulching</div>
  <div class="prog" style="top:58px">Pests &amp; Disease</div>
  <div class="prog" style="top:84px">Rubbish Removal</div>
  <div class="photo" role="img" aria-label="Gardener in a cap kneeling to pull weeds in a garden bed" style="left:10px;top:119px;width:150px;height:158px;background:linear-gradient(160deg,#556b3e,#7d8a5e 50%,#4a5a36)"></div>
  <div class="abs" style="left:10px;top:240px;width:150px;height:37px;background:rgba(90,110,70,.55)"></div>
  <div class="abs h-oswald" style="left:10px;top:244px;width:150px;text-align:center;color:#fff;font-size:7.5px;line-height:13px;font-weight:400">CALL US ANYTIME<br>
    <span style="display:inline-flex;align-items:center;gap:3px"><svg width="6" height="6" viewBox="0 0 10 10"><path d="M2 0.8 L3.8 3 L2.8 4.2 Q4 6.2 5.8 7.2 L7 6.2 L9.2 8 L8 9.6 Q3.5 9.6 0.6 2 Z" fill="#fff"/></svg>0400 555 182</span></div>
  <p class="abs" style="left:10px;top:288px;font-size:4.5px;letter-spacing:.6px;color:var(--green)">SERVICE DETAILS</p>
  <h2 class="abs h-oswald" style="left:10px;top:294px;font-size:12px;font-weight:400">Weed Control</h2>
  <p class="abs para" style="left:10px;top:314px;width:153px;font-size:5.4px">We provide weed control solutions for gardens, lawns and paved areas. We use a post emergent herbicide and we can combine that with a pre-emergent herbicide. We also provide non-chemical solutions.</p>
  <div class="photo" role="img" aria-label="Garden photo continuing below" style="left:10px;top:366px;width:150px;height:4px;background:#7a7050"></div>
</section>

<!-- Screen 3: Weed control continued -->
<section class="screen" style="left:518px">
  <div class="photo" role="img" aria-label="Weeds on paving being burned with a flame weeder" style="left:10px;top:0;width:150px;height:92px;background:linear-gradient(150deg,#a9a58d,#6f8f3a 55%,#c08a3a)"></div>
  <p class="abs para" style="left:10px;top:101px;width:154px">When a pre-emergent herbicide is applied to turf or gardens, the number of annual weeds is effectively reduced, thereby limiting the need to re-apply after the initial treatment. This also reduces the weed's seed bank that could potentially germinate in future years. Weed control is an essential aspect of having a well-presented garden, lawns, pathways and driveways.</p>
  <p class="abs" style="left:10px;top:188px;font-size:6.5px;color:var(--ink)">The additional services we offer to control weeds:</p>
  <div class="feat" style="left:10px;top:203px">
    <span><svg viewBox="0 0 12 12"><path d="M6 11V5M6 7Q2 7 1.5 3Q5 3 6 6M6 5Q6.5 1 10.5 1Q10.5 5 6 5" fill="none" stroke="#7dbb3c" stroke-width=".8"/></svg>Planting ground<br>cover plants</span>
    <span><svg viewBox="0 0 12 12"><path d="M6 11V5M6 7Q2 7 1.5 3Q5 3 6 6M6 5Q6.5 1 10.5 1Q10.5 5 6 5" fill="none" stroke="#7dbb3c" stroke-width=".8"/></svg>Solarisation</span>
    <span><svg viewBox="0 0 12 12"><path d="M6 11V5M6 7Q2 7 1.5 3Q5 3 6 6M6 5Q6.5 1 10.5 1Q10.5 5 6 5" fill="none" stroke="#7dbb3c" stroke-width=".8"/></svg>Mulching</span>
  </div>
  <p class="abs para" style="left:10px;top:224px;width:154px">Lorem ipsum dolor sit amet, consectetur adipiscing elit, seder do eiusmod tempor incididunt ut laboret.</p>
  <div class="photo" role="img" aria-label="Gloved hand pulling weeds from lawn" style="left:10px;top:258px;width:72px;height:52px;background:linear-gradient(135deg,#5f8a35,#8fb05a)"></div>
  <div class="photo" role="img" aria-label="Wheelbarrow on a lawn" style="left:88px;top:258px;width:72px;height:52px;background:linear-gradient(135deg,#6d8a45,#8b8a70)"></div>
  <div class="photo" role="img" aria-label="Hand spraying herbicide on weeds" style="left:10px;top:316px;width:72px;height:54px;background:linear-gradient(135deg,#8cc63f,#5c9a2c)"></div>
  <div class="photo" role="img" aria-label="Line trimmer cutting dandelions" style="left:88px;top:316px;width:72px;height:54px;background:linear-gradient(135deg,#6c9a3a,#4e7a2a)"></div>
</section>

<!-- Screen 4: Gallery and call to action -->
<section class="screen" style="left:736px">
  <div class="feat" style="left:10px;top:17px">
    <span><svg viewBox="0 0 12 12"><path d="M6 11V5M6 7Q2 7 1.5 3Q5 3 6 6M6 5Q6.5 1 10.5 1Q10.5 5 6 5" fill="none" stroke="#7dbb3c" stroke-width=".8"/></svg>Planting ground<br>cover plants</span>
    <span><svg viewBox="0 0 12 12"><path d="M6 11V5M6 7Q2 7 1.5 3Q5 3 6 6M6 5Q6.5 1 10.5 1Q10.5 5 6 5" fill="none" stroke="#7dbb3c" stroke-width=".8"/></svg>Solarisation</span>
    <span><svg viewBox="0 0 12 12"><path d="M6 11V5M6 7Q2 7 1.5 3Q5 3 6 6M6 5Q6.5 1 10.5 1Q10.5 5 6 5" fill="none" stroke="#7dbb3c" stroke-width=".8"/></svg>Mulching</span>
  </div>
  <p class="abs para" style="left:10px;top:40px;width:154px">Lorem ipsum dolor sit amet, consectetur adipiscing elit, seder do eiusmod tempor incididunt ut laboret.</p>
  <div class="photo" role="img" aria-label="Gloved hand pulling weeds from lawn" style="left:10px;top:72px;width:72px;height:53px;background:linear-gradient(135deg,#5f8a35,#8fb05a)"></div>
  <div class="photo" role="img" aria-label="Wheelbarrow on a lawn" style="left:88px;top:72px;width:72px;height:53px;background:linear-gradient(135deg,#6d8a45,#8b8a70)"></div>
  <div class="photo" role="img" aria-label="Hand spraying herbicide on weeds" style="left:10px;top:131px;width:72px;height:52px;background:linear-gradient(135deg,#8cc63f,#5c9a2c)"></div>
  <div class="photo" role="img" aria-label="Line trimmer cutting dandelions" style="left:88px;top:131px;width:72px;height:52px;background:linear-gradient(135deg,#6c9a3a,#4e7a2a)"></div>
  <p class="abs para" style="left:10px;top:191px;width:154px">Temporibus autem quibusdam et aut officiis debitis aut rerum necessitatibus saepe eveniet ut et voluptates repudiandae sint et molestiae non recusandae.</p>
  <div class="abs cta-box">
    <p class="abs cta-title">Is your garden overgrown with weeds?</p>
    <p class="abs" style="top:36px;width:100%;text-align:center;font-size:5.6px;color:var(--ink)">Hire us now, and we will take care of it!</p>
    <div class="abs btn" style="left:51px;top:52px;width:49px;height:19px">FREE QUOTE</div>
  </div>
  <div class="abs" style="left:10px;top:338px;width:151px;height:1px;background:#eee"></div>
  <p class="abs pager" style="left:10px;top:348px;color:var(--muted)">← PREVIOUS SERVICE</p>
  <p class="abs pager" style="right:10px;top:348px;color:var(--green)">NEXT SERVICE →</p>
</section>

<!-- Screen 5: Footer -->
<section class="screen s5" style="left:954px">
  <div class="abs brand" style="left:20px;top:44px;font-size:8.5px"><i style="width:8px;height:8px"></i>LARKVALE</div>
  <p class="abs" style="left:20px;top:68px;width:100px;font-size:5.6px;line-height:11.2px">Scheduled Garden Care Programs and Garden Maintenance Services for residential, strata and the commercial properties in Perth, WA</p>
  <h3 class="abs foot-h" style="left:20px;top:128px">Quick Links</h3>
  <div class="abs rule" style="left:20px;top:146px"></div>
  <p class="abs foot-link" style="left:20px;top:156px">Home</p>
  <p class="abs foot-link" style="left:20px;top:170px">About</p>
  <p class="abs foot-link" style="left:20px;top:184px">Services</p>
  <p class="abs foot-link" style="left:20px;top:199px">Work</p>
  <p class="abs foot-link" style="left:20px;top:213px">Contact</p>
  <h3 class="abs foot-h" style="left:20px;top:238px">Contact</h3>
  <div class="abs rule" style="left:20px;top:256px"></div>
  <p class="abs foot-link" style="left:20px;top:266px;display:flex;align-items:center;gap:4px"><svg width="5" height="5" viewBox="0 0 10 10"><path d="M2 0.8 L3.8 3 L2.8 4.2 Q4 6.2 5.8 7.2 L7 6.2 L9.2 8 L8 9.6 Q3.5 9.6 0.6 2 Z" fill="#7dbb3c"/></svg>0400 555 182</p>
  <p class="abs foot-link" style="left:20px;top:280px;display:flex;align-items:center;gap:4px"><svg width="5" height="4" viewBox="0 0 10 8"><rect width="10" height="8" fill="#7dbb3c"/><path d="M0 0 L5 4.5 L10 0" fill="none" stroke="#111" stroke-width="1"/></svg>maya@larkvale.com.au</p>
  <div class="abs" style="left:20px;top:300px;width:120px;height:1px;background:#2a2a2a"></div>
  <p class="abs foot-link" style="left:20px;top:311px;font-size:5.4px">Find Us Also At:</p>
  <div class="abs social" style="left:20px;top:323px"></div>
  <div class="abs social" style="left:39px;top:323px;background:var(--green)"></div>
  <div class="abs social" style="left:58px;top:323px"></div>
</section>

</body>
</html>
```